Bravo Glazing

We need a website design for a company based in Texas that specializes in doors and and windows.
Bravo Glazing is a leading window manufacturer of aluminum and vinyl windows, both serving the replacement and new construction markets. Bravo Glazing Inc. was created over 25 years ago when two existing window manufacturers with excellent reputations in their fields - merged. Bravo Glazing offers a complete line conforming to the needs of residential and commercial window markets.
The final design should be something that communicates professionalism and features they're key value propositions.
Example websites we like:
http://layouts.pebblecraft.example/qx/purse/
http://layouts.pebblecraft.example/qx/splashzone/
http://layouts.pebblecraft.example/qx/refit2/
This design should format the existing content to be more visually organized, improve the fonts to clearer and more readable, and make it easier for users to find services.
Brand guide is attached
Website images can be found here: https://share.vaultdrop.example/7kRtQmZxLpWeYb
Target Market(s)
Windows
Number of Pages Required
1 page
Look and feel
Each slider illustrates characteristics of the customer's brand and the style your logo design should communicate.

```html
<!DOCTYPE html>
<html lang="en">
<head>
<meta charset="utf-8">
<title>Bravo Glazing</title>
<link href="https://fonts.googleapis.com/css2?family=Raleway:wght@200;300;400;500&display=swap" rel="stylesheet">
<style>
  :root {
    --gold: #d4b45a;
    --ink: #3b3b3e;
    --muted: #8d8d8d;
    --shadow: #e9e9e9;
    --white: #ffffff;
  }
  html, body { margin: 0; padding: 0; overflow: hidden; background: var(--white); }
  .page {
    position: relative; width: 1200px; height: 1200px; overflow: hidden;
    font-family: 'Raleway', sans-serif; color: var(--ink); background: var(--white);
  }
  .abs { position: absolute; }
  .hero-shape { left: 0; top: 0; }
  .brand {
    left: 124px; top: 48px; font-size: 22px; font-weight: 400; color: var(--white);
    letter-spacing: 0.5px; display: flex; align-items: center; gap: 8px; white-space: nowrap;
  }
  .brand .mark { width: 9px; height: 9px; border-radius: 50%; background: var(--white); }
  .nav-item { top: 51px; font-size: 13px; letter-spacing: 1.2px; font-weight: 400; color: #4a4a4c; white-space: nowrap; }
  .nav-dots { left: 450px; top: 68px; display: flex; gap: 3px; }
  .nav-dots span { width: 3px; height: 3px; border-radius: 50%; background: #4a4a4c; }
  .headline {
    left: 262px; top: 282px; margin: 0; font-size: 37px; font-weight: 300;
    line-height: 44px; letter-spacing: 0.4px; color: var(--ink); white-space: nowrap;
  }
  .view-more {
    left: 574px; top: 400px; font-size: 16px; font-weight: 400; color: var(--ink);
    letter-spacing: 0.4px; white-space: nowrap;
  }
  .view-more-rule { left: 590px; top: 429px; width: 58px; height: 1px; background: #6b6350; }
  .section-title { margin: 0; font-weight: 300; letter-spacing: 2px; color: #2e2e30; white-space: nowrap; }
  .accent { color: var(--gold); }
  .who-title { right: 156px; top: 509px; font-size: 21px; }
  .who-copy {
    left: 686px; top: 550px; width: 358px; margin: 0; font-size: 13.5px; line-height: 16.4px;
    letter-spacing: 1.6px; color: var(--muted); text-align: justify; font-weight: 400;
  }
  .text-link {
    font-size: 13.6px; letter-spacing: 1px; color: #2e2e30; font-weight: 400; white-space: nowrap;
    padding: 6px 0 8px 9px; border-left: 1px solid #555; border-bottom: 1px solid #555;
  }
  .know-more { left: 944px; top: 652px; width: 79px; }
  .work-shadow { background: var(--shadow); }
  .work-title { top: 844px; font-size: 46px; font-weight: 200; letter-spacing: 2px; line-height: 1; margin: 0; white-space: nowrap; }
  .work-title.on-photo { left: 570px; color: var(--white); }
  .work-title.accent { left: 686px; color: var(--gold); }
  .work-copy {
    left: 707px; top: 916px; width: 370px; margin: 0; font-size: 13px; line-height: 16.5px;
    letter-spacing: 1.2px; color: var(--muted);
  }
  .see-more { left: 829px; top: 996px; width: 70px; }
</style>
</head>
<body>
<div class="page">
  <svg class="abs hero-shape" width="1200" height="1200" viewBox="0 0 1200 1200" role="img" aria-label="Modern kitchen interior photo tinted in gold">
    <defs>
      <linearGradient id="heroTint" x1="0" y1="0" x2="1" y2="1">
        <stop offset="0" stop-color="#d6b862"/>
        <stop offset="0.5" stop-color="#d3b45c"/>
        <stop offset="1" stop-color="#cfae55"/>
      </linearGradient>
    </defs>
    <polygon points="60,0 1141,0 1141,396 60,698" fill="url(#heroTint)"/>
    <rect x="60" y="1168" width="1081" height="32" fill="url(#heroTint)"/>
  </svg>

  <div class="abs brand"><span>Bravo Glazing</span><span class="mark"></span></div>

  <nav>
    <span class="abs nav-item" style="left:438px">HOME</span>
    <span class="abs nav-item" style="left:519px">SERVICE</span>
    <span class="abs nav-item" style="left:627px">PORTFOLIO</span>
    <span class="abs nav-item" style="left:762px">SHOP</span>
    <span class="abs nav-item" style="left:842px">BLOG</span>
    <span class="abs nav-item" style="left:923px">ABOUT</span>
    <span class="abs nav-item" style="left:1008px">CONTACT</span>
    <div class="abs nav-dots"><span></span><span></span><span></span></div>
  </nav>

  <svg class="abs" style="left:0;top:0" width="1200" height="600" viewBox="0 0 1200 600">
    <rect x="178.5" y="187.5" width="268" height="303" fill="none" stroke="#4c4a46" stroke-width="1"/>
    <rect x="154.5" y="214.5" width="268" height="302" fill="none" stroke="#4c4a46" stroke-width="1"/>
  </svg>

  <h1 class="abs headline">Walking with a friend in the dark is<br>better than alone in the light.</h1>
  <span class="abs view-more">View More</span>
  <div class="abs view-more-rule"></div>

  <h2 class="abs section-title who-title">WHO WE <span class="accent">ARE</span>?</h2>
  <p class="abs who-copy">Lorem Ipsum is simply dummy text of the printing and typesetting industry. Lorem Ipsum has been the industry's standard dummy text ever since the 1500s, when an unknown printer took a galley of type and type.</p>
  <span class="abs text-link know-more">Know More</span>

  <div class="abs work-shadow" style="left:142px;top:766px;width:158px;height:298px"></div>
  <div class="abs work-shadow" style="left:330px;top:766px;width:157px;height:298px"></div>
  <div class="abs work-shadow" style="left:514px;top:764px;width:157px;height:298px"></div>

  <div class="abs" role="img" aria-label="Dim living room with sliding glass doors and lounge chairs" style="left:152px;top:755px;width:158px;height:297px;background:linear-gradient(180deg,#34384a 0%,#4f4c4c 45%,#6e6555 70%,#4a443c 100%)"></div>
  <div class="abs" role="img" aria-label="Open-plan kitchen and living room with white sofa" style="left:339px;top:754px;width:155px;height:297px;background:linear-gradient(180deg,#6d6a69 0%,#807975 45%,#8c8580 75%,#7a6460 100%)"></div>
  <div class="abs" role="img" aria-label="Brick house exterior with large windows" style="left:522px;top:754px;width:155px;height:297px;background:linear-gradient(180deg,#3c4a60 0%,#4e4d52 40%,#6a5f58 75%,#5a5d48 100%)"></div>

  <h2 class="abs work-title on-photo">OUR</h2>
  <h2 class="abs work-title accent">WORK</h2>
  <p class="abs work-copy">Lorem Ipsum is simply dummy text of the printing and typesetting industry. Lorem Ipsum has been the industry's standard dummy...</p>
  <span class="abs text-link see-more">See More</span>
</div>
</body>
</html>
```